Re-design of Business Card

We require a design for our business card.

Korrim is a supplier of industrial packaging specializing in plastic products. We are undergoing a rebranding to appear more corporate. We have changed our company name to korrim and have a new logo.

I have uploaded our old card design with the previous company name.
Don't copy the current design. We are looking for a new design.

Industry/Entity Type

Manufacturing

Contact Information for Business Card

please don't copy the current design. we are looking for a new design.

Font styles to use
Sans Serif

Colors

Designer to choose colors to be used in the design.

Requirements
Must have
• clean and easy to read.

```html
<!DOCTYPE html>
<html lang="en">
<head>
<meta charset="UTF-8">
<title>Korrim Business Card</title>
<link href="https://fonts.googleapis.com/css2?family=Open+Sans:wght@400;700&display=swap" rel="stylesheet">
<style>
  :root {
    --bg: #d9d9d9;
    --card-dark: #2a2a2a;
    --card-light: #ffffff;
    --accent: #f07c1c;
    --ink: #1e1e1e;
    --muted: #555555;
  }
  * { box-sizing: border-box; margin: 0; padding: 0; }
  html, body {
    width: 1200px; height: 900px; overflow: hidden;
    background: var(--bg);
    font-family: "Open Sans", sans-serif;
  }
  .canvas { position: relative; width: 1200px; height: 900px; }
  .card {
    position: absolute; left: 280px; width: 640px; height: 390px;
    box-shadow: 0 6px 18px rgba(0,0,0,.25);
  }
  .card--front { top: 25px; background: var(--card-dark); display: flex; align-items: center; justify-content: center; }
  .brand-name {
    color: var(--accent); font-weight: 700; font-size: 64px; letter-spacing: 2px;
  }
  .card--back { top: 485px; background: var(--card-light); }
  .identity {
    position: absolute; left: 60px; top: 118px; width: 222px; text-align: right;
  }
  .person-name { color: var(--accent); font-weight: 700; font-size: 21px; letter-spacing: .5px; line-height: 1.15; white-space: nowrap; }
  .person-role { color: var(--ink); font-size: 14px; margin-top: 1px; white-space: nowrap; }
  .address { color: var(--muted); font-size: 14px; line-height: 1.3; margin-top: 6px; }
  .divider {
    position: absolute; left: 302px; top: 120px; width: 2px; height: 150px; background: var(--accent);
  }
  .contacts {
    position: absolute; left: 322px; top: 122px; list-style: none;
  }
  .contact-item {
    display: flex; align-items: center; gap: 6px;
    color: var(--muted); font-size: 15px; line-height: 28px; white-space: nowrap;
  }
  .contact-icon { width: 14px; height: 14px; fill: var(--accent); flex: none; }
</style>
</head>
<body>
<div class="canvas">
  <section class="card card--front">
    <span class="brand-name">KORRIM</span>
  </section>

  <section class="card card--back">
    <div class="identity">
      <div class="person-name">DANA WHITFIELD</div>
      <div class="person-role">Machinery Sales Manager</div>
      <div class="address">48 Harlow St<br>Brookfield Vale, Qld<br>4170 Australia</div>
    </div>
    <div class="divider"></div>
    <ul class="contacts">
      <li class="contact-item">
        <svg class="contact-icon" viewBox="0 0 16 16"><path d="M3.5 1l2.5 3-1.5 1.5c.8 2 2.5 3.7 4.5 4.5L10.5 8.5l3 2.5-1.5 3C6.5 14 2 9.5 2 2.5z"/></svg>
        1300 418 226
      </li>
      <li class="contact-item">
        <svg class="contact-icon" viewBox="0 0 16 16"><rect x="4" y="1" width="8" height="4"/><rect x="1" y="6" width="14" height="6" rx="1"/><rect x="4" y="10" width="8" height="5" fill="#fff" stroke="#f07c1c" stroke-width="1.5"/></svg>
        +61 7 3540 2917
      </li>
      <li class="contact-item">
        <svg class="contact-icon" viewBox="0 0 16 16"><path d="M4 1h8v14H4z M5.5 2.5v9h5v-9z"/></svg>
        1300 418 226
      </li>
      <li class="contact-item">
        <svg class="contact-icon" viewBox="0 0 16 16"><path d="M1 3h14v1.5L8 9 1 4.5z M1 6.2l7 4.5 7-4.5V13H1z"/></svg>
        dana@korrim.com.au
      </li>
      <li class="contact-item">
        <svg class="contact-icon" viewBox="0 0 16 16"><circle cx="8" cy="8" r="7"/><path d="M5 4c2 0 2 2 4 2s1 3-1 3-1 3-3 3" fill="none" stroke="#fff" stroke-width="1.4"/></svg>
        www.korrim.com.au
      </li>
    </ul>
  </section>
</div>
</body>
</html>
```